Marlo Tidy Yard Website

We need a website design for this new company. I've attached the company logo. This company is in the construction industry that provides general labor, maintenance and cleaning for construction sites. We want a clean and simple website that can be easy to navigate.

Target Market(s)

Construction industry

Industry/Entity Type

Construction

Number of Pages Required

2 page

Font styles to use
Sans Serif

```html
<!DOCTYPE html>
<html lang="en">
<head>
<meta charset="utf-8">
<title>Marlo Tidy Yard</title>
<link href="https://fonts.googleapis.com/css2?family=Rubik:wght@300;400;500;700&display=swap" rel="stylesheet">
<style>
:root{
  --navy:#0d0d6b;
  --navy-text:#1c1c5e;
  --orange:#ff6a00;
  --white:#ffffff;
  --muted:#9a9ab0;
  --field:#f6f6fa;
  --line:#e6e6ef;
  --lavender:#f7f7fd;
  --ink:#333344;
}
*{box-sizing:border-box;margin:0;padding:0}
html,body{width:960px;height:1200px;overflow:hidden;background:var(--white);font-family:'Rubik',sans-serif;color:var(--ink)}
.screen{position:absolute;left:30px;width:750px;height:468px;overflow:hidden;background:var(--white);transform:scale(1.2);transform-origin:0 0;box-shadow:0 0 0 1px var(--line)}
.screen--home{top:25px}
.screen--services{top:613px}
.abs{position:absolute}

.topbar{left:0;top:0;width:750px;height:21px;background:var(--navy);color:var(--white);font-size:6px}
.topbar .item{position:absolute;top:7px;display:flex;align-items:center;gap:4px}
.topbar .phone{left:73px}
.topbar .service{left:157px}
.social{position:absolute;right:72px;top:6px;display:flex;gap:11px}
.social span{width:8px;height:8px;border-radius:50%;background:var(--white)}

.header{left:0;top:21px;width:750px;height:33px;border-bottom:1px solid var(--line)}
.brand{position:absolute;left:73px;top:8px;display:flex;align-items:center;gap:4px;font-weight:700;font-size:9px;color:var(--navy);letter-spacing:.1px}
.brand i{width:8px;height:8px;background:var(--orange)}
.nav{position:absolute;top:12px;font-size:7px;color:var(--navy-text)}
.nav.active{font-weight:500}
.nav.active::after{content:"";position:absolute;left:0;right:0;top:15px;height:2px;background:var(--orange)}
.caret{font-size:5px;color:var(--muted);margin-left:2px}

.subbar{left:0;top:54px;width:750px;height:33px}
.btn-quote{position:absolute;left:73px;top:0;width:93px;height:33px;background:var(--orange);color:var(--white);font-size:7px;font-weight:500;display:flex;align-items:center;justify-content:center}
.search{position:absolute;left:166px;top:0;width:279px;height:33px;background:var(--field);display:flex;align-items:center;padding-left:18px;gap:8px;font-size:7px;color:var(--muted)}
.subnav{position:absolute;top:12px;font-size:7px;color:var(--navy-text)}

.hero{left:0;top:87px;width:750px;height:320px}
.hero-photo{position:absolute;inset:0;background:linear-gradient(135deg,#5a5a5a 0%,#3a3a3a 35%,#6b6b6b 60%,#404040 100%)}
.hero-title{position:absolute;left:73px;top:56px;color:var(--white);font-size:19px;font-weight:700}
.hero-sub{position:absolute;left:73px;top:83px;color:var(--white);font-size:13px;font-weight:300}
.hero-btn{position:absolute;top:120px;height:31px;display:flex;align-items:center;justify-content:center;color:var(--white);font-size:7px;font-weight:500}
.hero-btn.cases{left:73px;width:124px;background:var(--orange)}
.hero-btn.services{left:203px;width:125px;background:var(--navy)}
.dots{position:absolute;left:38px;top:118px;display:flex;flex-direction:column;gap:7px}
.dots span{width:5px;height:5px;border-radius:50%;border:1px solid var(--white)}
.hero-wave{position:absolute;left:0;top:0}

.quote{left:481px;top:107px;width:196px;height:224px;background:var(--white);border-radius:3px;padding:10px 16px;box-shadow:0 2px 8px rgba(0,0,0,.15)}
.quote h3{font-size:8px;font-weight:500;color:var(--navy-text);margin-bottom:9px}
.field{height:19px;border:1px solid var(--line);margin-bottom:7px;font-size:5px;color:var(--muted);padding:6px 6px;position:relative}
.field.select::after{content:"▾";position:absolute;right:5px;top:5px;font-size:6px}
.field.area{height:48px}
.enquire{height:22px;background:var(--orange);color:var(--white);font-size:7px;display:flex;align-items:center;justify-content:center;margin-top:2px}

.section-title{position:absolute;left:73px;font-size:19px;font-weight:300;color:var(--navy-text)}
.lorem{position:absolute;left:328px;width:350px;font-size:8.2px;line-height:14.5px;color:var(--navy-text)}

.service-icon{position:absolute;width:46px;height:46px;border-radius:50%;border:2px solid var(--orange);display:flex;align-items:center;justify-content:center}
.service-label{position:absolute;width:80px;text-align:center;font-size:8.5px;color:var(--ink)}

.features{left:0;top:218px;width:750px;height:250px}
.feature-icon{position:absolute}
.feature-title{position:absolute;width:160px;text-align:center;font-size:9.5px;font-weight:500;color:#2a2a3a;letter-spacing:.3px}
.feature-text{position:absolute;width:160px;text-align:center;font-size:6.8px;line-height:11.5px;color:var(--navy-text)}
.slide-line{left:322px;top:466px;width:105px;height:2px;background:var(--navy)}
</style>
</head>
<body>

<!-- Home screen -->
<section class="screen screen--home">
  <div class="abs topbar">
    <span class="item phone"><svg width="6" height="6" viewBox="0 0 10 10"><path d="M2 1l2 2-1 1.5c.8 1.5 1.8 2.5 3 3L7.5 6l2 2-1.5 1.5C4 9 1 6 .5 1.5z" fill="#fff"/></svg>555-010-2040</span>
    <span class="item service"><svg width="8" height="6" viewBox="0 0 12 9"><rect x=".5" y=".5" width="11" height="8" fill="none" stroke="#fff"/><path d="M.5 .5l5.5 4.5 5.5-4.5" fill="none" stroke="#fff"/></svg>Customer Service</span>
    <div class="social" aria-label="Social links"><span></span><span></span><span></span></div>
  </div>
  <header class="abs header">
    <div class="brand"><i></i>Marlo Tidy Yard</div>
    <span class="nav active" style="left:450px">Home</span>
    <span class="nav" style="left:508px">About Us</span>
    <span class="nav" style="left:568px">Services<span class="caret">▼</span></span>
    <span class="nav" style="left:633px">Contact us</span>
  </header>
  <div class="abs subbar">
    <div class="btn-quote">GET A QUOTE</div>
    <div class="search"><svg width="8" height="8" viewBox="0 0 10 10"><circle cx="4" cy="4" r="3" fill="none" stroke="#555" stroke-width="1.2"/><path d="M6.3 6.3L9 9" stroke="#555" stroke-width="1.2"/></svg>Search</div>
    <span class="subnav" style="left:466px">Our Blog</span>
    <span class="subnav" style="left:523px">Promotions<span class="caret">▼</span></span>
    <span class="subnav" style="left:600px">Pricing</span>
    <span class="subnav" style="left:650px">Claims</span>
  </div>
  <div class="abs hero">
    <div class="hero-photo" role="img" aria-label="Aerial photo of a construction site with workers in safety gear"></div>
    <svg class="hero-wave" width="750" height="320" viewBox="0 0 750 320">
      <path d="M0 240 C120 228 220 250 330 252 C450 255 580 225 750 228 L750 320 L0 320 Z" fill="var(--orange)"/>
      <path d="M0 272 C140 240 300 285 440 300 C560 310 660 290 750 275 L750 320 L0 320 Z" fill="var(--white)"/>
    </svg>
    <h1 class="hero-title">We help you</h1>
    <p class="hero-sub">Focusing on Your Construction</p>
    <div class="dots"><span></span><span></span><span></span></div>
    <div class="hero-btn cases">VIEW OUR CASES</div>
    <div class="hero-btn services">VIEW OUR SERVICES</div>
  </div>
  <form class="abs quote">
    <h3>Get a Quote Now</h3>
    <div class="field">Tell us your name</div>
    <div class="field">Your Email</div>
    <div class="field select">Services Required</div>
    <div class="field select">Construction Site Location</div>
    <div class="field area">Additional info you want to tell us</div>
    <div class="enquire">ENQUIRE</div>
  </form>
  <h2 class="section-title" style="top:410px">Get your need for the best price</h2>
  <div class="service-icon" style="left:73px;top:456px"></div>
  <div class="service-icon" style="left:151px;top:456px"></div>
  <div class="service-icon" style="left:222px;top:456px"></div>
  <p class="lorem" style="top:456px">Lorem ipsum dolor sit amet, consectetur adipiscing elit, sed do eiusmod tempor</p>
</section>

<!-- Services screen -->
<section class="screen screen--services">
  <div class="abs topbar">
    <span class="item phone"><svg width="6" height="6" viewBox="0 0 10 10"><path d="M2 1l2 2-1 1.5c.8 1.5 1.8 2.5 3 3L7.5 6l2 2-1.5 1.5C4 9 1 6 .5 1.5z" fill="#fff"/></svg>555-010-2040</span>
    <span class="item service"><svg width="8" height="6" viewBox="0 0 12 9"><rect x=".5" y=".5" width="11" height="8" fill="none" stroke="#fff"/><path d="M.5 .5l5.5 4.5 5.5-4.5" fill="none" stroke="#fff"/></svg>Customer Service</span>
    <div class="social" aria-label="Social links"><span></span><span></span><span></span></div>
  </div>
  <header class="abs header">
    <div class="brand"><i></i>Marlo Tidy Yard</div>
    <span class="nav active" style="left:450px">Home</span>
    <span class="nav" style="left:508px">About Us</span>
    <span class="nav" style="left:568px">Services<span class="caret">▼</span></span>
    <span class="nav" style="left:633px">Contact us</span>
  </header>
  <svg class="abs" style="left:400px;top:54px" width="270" height="14" viewBox="0 0 270 14"><path d="M10 0 C80 14 190 14 260 0 Z" fill="var(--orange)"/></svg>

  <h2 class="section-title" style="top:88px">Get your need for the best price</h2>
  <div class="service-icon" style="left:73px;top:135px">
    <svg width="24" height="24" viewBox="0 0 24 24" fill="none" stroke="var(--orange)" stroke-width="1.4"><circle cx="11" cy="7" r="3.5"/><path d="M4 20c1-5 4-7 7-7s5 1 6 3M15 17l3 2 3-3"/></svg>
  </div>
  <div class="service-icon" style="left:151px;top:135px">
    <svg width="24" height="24" viewBox="0 0 24 24" fill="none" stroke="var(--orange)" stroke-width="1.4"><path d="M15 3a5 5 0 0 0-5 6L3 16a2 2 0 0 0 3 3l7-7a5 5 0 0 0 6-5l-3 2-3-1-1-3z"/></svg>
  </div>
  <div class="service-icon" style="left:222px;top:135px">
    <svg width="24" height="24" viewBox="0 0 24 24" fill="none" stroke="var(--orange)" stroke-width="1.4"><rect x="4" y="9" width="16" height="11"/><path d="M9 9V4h6v5M4 14h16M12 12v4"/></svg>
  </div>
  <span class="service-label" style="left:56px;top:189px">Labor</span>
  <span class="service-label" style="left:134px;top:189px">Maintenance</span>
  <span class="service-label" style="left:205px;top:189px">Cleaning</span>
  <p class="lorem" style="top:134px">Lorem ipsum dolor sit amet, consectetur adipiscing elit, sed do eiusmod tempor incididunt ut labore et dolore magna aliqua. Ut enim ad minim veniam, quis nostrud exercitation ullamco laboris nisi ut aliquip ex ea commodo consequat.</p>

  <div class="abs features">
    <svg class="abs" style="left:0;top:0" width="750" height="250" viewBox="0 0 750 250"><path d="M0 25 C200 5 450 -5 750 20 L750 250 L0 250 Z" fill="var(--lavender)"/></svg>

    <svg class="feature-icon" style="left:124px;top:68px" width="92" height="92" viewBox="0 0 92 92" fill="none" stroke="var(--navy)" stroke-width="1.2">
      <path d="M46 1 L91 46 L46 91 L1 46 Z"/>
      <path d="M56 38a14 14 0 1 1-6-7"/><path d="M46 36v11l6 4"/><path d="M55 32l2-1M58 36l1-1" stroke-dasharray="1 2"/>
    </svg>
    <div class="feature-title" style="left:90px;top:173px">EFFICIENCY</div>
    <p class="feature-text" style="left:90px;top:192px">We've made process as simple as possible, it only takes you 2 minutes to complete the form.</p>

    <svg class="feature-icon" style="left:329px;top:48px" width="92" height="92" viewBox="0 0 92 92" fill="none" stroke="var(--navy)" stroke-width="1.2">
      <path d="M46 1 L91 46 L46 91 L1 46 Z"/>
      <path d="M28 32 L64 32 L46 64 Z"/><path d="M34 35 L46 44 L58 35 M46 44 L46 60"/>
    </svg>
    <div class="feature-title" style="left:295px;top:153px">CAPACITY</div>
    <p class="feature-text" style="left:295px;top:172px">We provide the capability to service all types of services:general labor, maintenance and cleanning,...</p>

    <svg class="feature-icon" style="left:532px;top:68px" width="92" height="92" viewBox="0 0 92 92" fill="none" stroke="var(--navy)" stroke-width="1.2">
      <path d="M46 1 L91 46 L46 91 L1 46 Z"/>
      <circle cx="46" cy="46" r="6"/><circle cx="46" cy="46" r="10"/>
      <path d="M46 30l3 4 5-1 1 5 4 3-3 4 3 4-4 3-1 5-5-1-3 4-3-4-5 1-1-5-4-3 3-4-3-4 4-3 1-5 5 1z"/>
    </svg>
    <div class="feature-title" style="left:498px;top:173px">CUSTOMIZED</div>
    <p class="feature-text" style="left:498px;top:187px">We provide a variety of services for your site and you are free to choose what you want</p>
  </div>
  <div class="abs slide-line"></div>
</section>

</body>
</html>
```